Brivora Distance Learning Website

Brivora provide e-learning and mixed learning solutions for individuals, colleges, organisations and B2B.
We need a modern, light and flat website design for Brivora. We want to to see the designer incorporate user experience(UX) design elements into the AI or PSD mockups. We would like to see designs that use pastel colors that compliment yellow and black of our logo.
We want our E-learning experience to accelerate learning and for the interface to be user friendly and intuitive. We want the designs to focus on quick access to course information, course reviews, learning progress and study advice. Quick and intuitive access to all content for our clients is one of our top priorities.
We would like designs for the following project 3 pages:
1. Learner homepage dashboard (see attached screenshot).
On this page the Learners need to:
- Login
- Have quick access to Packages and Courses.
- See other recommended courses (Below Packages and Courses)
- Possibly a left hand side column/menu with thumbnail icons (See lumivex learner dashboard screenshot)
2. Homepage
See current sample
http://www.brivora-learn.test
We would like the designer to focus on creating a customized banner to enhance the home page.
3. Primary Landing/Marketing page
This page is geared towards customer acquisition with the focal point being the top banner (video or HD image).
And Course Preview content below.
See reference
http://brivora-learn.test/subscriptionPlans/marketing/MTc%3D/Mjc4Nw%3D%3D/Quick%20Fennish%20%2B%20Fennish%20Nibbles%20Bundle%20by%20Harold%20Wen%20Pike
Other site we like:
- https://www.korvanta.test (We like the home page and top bar on courses page)
- http://www.tutorglen.test
- http://crewmapleden.test (think this site looks great, love the lower graphics on the homepage)
Updates
Hello,
Thank you for taking the time to contribute to this web design competition. We would just like to point out a few things:
1. Please try to make the color palette similar to the colors used in the screenshot that we just uploaded ('possible color palette).
2. Please make the designs specific to each page: THE LEARNER HOMEPAGE, HOME PAGE, and the MARKETING LANDING PAGE.
We are very happy with the high quality of designs so far,
Cheers,
Lee Ab
KV-Studio
Also,
Please avoid using dark/bold elements in the designs. The ONLY elements that we want to be dark are the logo and the footer.
Any questions please ask,
Cheers,
Lee Ab
Kv-Studio
Hello,
Based on the round of feedback we just gave it would be great if you could complete further design changes by tomorrow, as we are pushed for time.
Thank you,
Lee Ab
KV-Studio

```html
<!DOCTYPE html>
<html lang="en">
<head>
<meta charset="utf-8">
<title>Brivora — E-learning and Mixed Learning</title>
<link rel="stylesheet" href="https://fonts.googleapis.com/css2?family=Open+Sans:ital,wght@0,300;0,400;0,600;0,700;0,800;1,400&display=swap">
<style>
:root{
  --ink:#1b1b1b;
  --text:#555;
  --muted:#8a8a8a;
  --line:#e3e3e3;
  --yellow:#f7b21b;
  --orange:#f39a1e;
  --blue:#5aa1dc;
  --blue-deep:#3a7fc4;
  --teal:#1fbc9c;
  --sky:#5fb0e8;
  --red:#d9473a;
  --taupe:#aca69f;
  --footer:#474747;
  --footer-deep:#3a3a3a;
  --white:#fff;
}
*{box-sizing:border-box;margin:0;padding:0}
html,body{width:1200px;height:4079px;overflow:hidden}
body{font-family:"Open Sans",Arial,sans-serif;color:var(--text);background:var(--white);position:relative}
section,header,footer{position:absolute;left:0;width:1200px}
.abs{position:absolute}

/* header */
.site-header{top:0;height:75px;background:var(--white);border-bottom:1px solid var(--line)}
.menu-block{left:0;top:0;width:120px;height:75px;background:var(--ink)}
.menu-block span{position:absolute;left:38px;width:40px;height:5px;background:var(--white);border-radius:2px}
.brand{left:140px;top:18px;height:40px;display:flex;align-items:center;color:var(--ink);font-weight:700;font-size:26px;letter-spacing:.3px}
.top-nav{right:85px;top:20px;display:flex;gap:28px;font-size:15px;color:var(--ink)}
.top-nav a{color:inherit;text-decoration:none;padding-bottom:6px}
.top-nav a.active{border-bottom:3px solid var(--yellow)}

/* hero */
.hero{top:75px;height:605px}
.hero-photo{position:absolute;inset:0;background:linear-gradient(100deg,#2b3033 0%,#353b3f 45%,#4a4f52 70%,#3a3f42 100%)}
.hero-intro{left:85px;top:105px;width:620px;color:var(--white);font-size:23px;line-height:1.45;font-weight:400}
.watch{display:inline-flex;align-items:center;gap:8px;color:var(--orange);font-size:14px;font-weight:700;margin-left:14px;vertical-align:middle}
.watch i{width:22px;height:22px;border-radius:50%;background:#111;display:inline-flex;align-items:center;justify-content:center}
.hero-title{left:85px;top:255px;color:var(--white);font-size:32px;line-height:1.25;font-weight:800;letter-spacing:.5px}
.join{left:85px;top:350px;width:240px;height:58px;background:var(--orange);border-radius:4px;color:var(--white);font-size:24px;font-weight:700;display:flex;align-items:center;justify-content:center}
.search{left:200px;top:470px;width:800px;height:70px;background:rgba(20,22,24,.78);border-radius:3px;display:flex;align-items:center;padding:0 30px;justify-content:space-between}
.search span{color:#8b8f93;font-size:22px;font-style:italic}

/* highlights */
.highlights{top:680px;height:290px;border-bottom:1px solid var(--line)}
.highlight{position:absolute;top:70px;width:300px;text-align:center}
.highlight svg{display:block;margin:0 auto 22px}
.highlight h3{font-size:16px;font-weight:400;color:#444;margin-bottom:12px}
.highlight p{font-size:12px;line-height:1.5;color:var(--muted)}

/* packages */
.packages{top:970px;height:590px}
.section-title{position:absolute;left:0;width:1200px;text-align:center;font-size:32px;font-weight:300;color:#666}
.pack-tabs{left:85px;top:80px;width:1037px;height:40px;border-bottom:1px solid var(--line)}
.pack-tabs .tab{position:absolute;left:0;top:6px;font-size:16px;font-weight:600;color:var(--blue-deep);padding-bottom:10px;border-bottom:3px solid var(--yellow)}
.pack-arrows{position:absolute;right:0;top:4px;display:flex;gap:6px}
.pack-arrows i{width:24px;height:24px;background:#8c8c8c;display:flex;align-items:center;justify-content:center}
.card{position:absolute;top:125px;width:242px;height:316px;border:1px solid #ddd;border-radius:4px;background:var(--white);overflow:hidden}
.card-cover{height:118px;display:flex;align-items:center;justify-content:center;position:relative}
.card-cover .fav{position:absolute;right:8px;top:8px;width:18px;height:18px;background:rgba(255,255,255,.6)}
.card p{font-size:13px;line-height:1.45;color:#444;padding:14px 14px 0}
.card .date{font-size:11px;color:var(--muted);padding:14px 14px 0}
.card-meta{position:absolute;left:14px;right:14px;bottom:12px;border-top:1px solid var(--line);padding-top:10px;display:flex;align-items:center;gap:16px;font-size:11px;color:var(--muted)}
.card-meta b{margin-left:auto;color:var(--orange);font-size:24px;font-weight:700}
.browse{left:340px;top:485px;width:520px;height:68px;border-radius:4px;background:linear-gradient(#b5b5b5,#8f8f8f);color:var(--white);font-size:24px;display:flex;align-items:center;justify-content:center}

/* how it works */
.how{top:1565px;height:475px;background:var(--taupe)}
.how-art{left:40px;top:40px;width:520px;height:400px;background:linear-gradient(160deg,#c8c3bd,#b7b1aa);border-radius:2px}
.how h2{position:absolute;left:680px;top:50px;color:var(--white);font-size:32px;font-weight:400}
.how p{position:absolute;left:680px;width:440px;color:var(--white);font-size:11px;line-height:1.6}

/* progress */
.progress{top:2040px;height:680px}
.progress .lead{position:absolute;left:200px;width:800px;top:100px;text-align:center;font-size:17px;line-height:1.5;color:#444}
.skill-label{position:absolute;width:200px;text-align:center;font-size:12px;color:var(--muted)}

/* devices */
.devices{top:2737px;height:476px}
.devices-photo{position:absolute;inset:0;background:linear-gradient(100deg,#6f6a62 0%,#8b867d 40%,#5f5a53 70%,#3c3a38 100%)}
.devices h2{position:absolute;left:85px;width:520px;text-align:center;top:45px;color:var(--white);font-size:34px;font-weight:600}
.devices p{position:absolute;left:85px;top:105px;width:520px;color:var(--white);font-size:19px;line-height:1.35;text-align:center}
.badge{position:absolute;top:325px;height:52px;border-radius:5px}

/* testimonials */
.voices{top:3213px;height:459px}
.voice{position:absolute;width:420px;height:140px}
.voice .name{position:absolute;left:140px;top:8px;font-size:19px;color:#444}
.voice .quote{position:absolute;left:140px;top:44px;width:270px;font-size:12px;line-height:1.5;color:var(--muted)}

/* footer */
.site-footer{top:3672px;height:407px;background:var(--footer);color:#ddd}
.site-footer .bar{position:absolute;left:0;bottom:0;width:1200px;height:40px;background:var(--footer-deep)}
.foot-links{left:85px;top:85px;list-style:none;font-size:12px;line-height:2.05;color:var(--white)}
.foot-col h4{font-size:17px;font-weight:600;color:var(--white);margin-bottom:18px}
.foot-col p{font-size:11px;line-height:1.6;color:#cfcfcf}
.tweet{display:flex;gap:10px;margin-bottom:14px}
.tweet i{width:14px;height:14px;border-radius:50%;background:#63b6e8;flex:none;margin-top:2px}
.field{width:160px;height:28px;background:#eee;border-radius:2px}
.go{width:40px;height:28px;background:var(--yellow)}
.social{display:flex;gap:5px}
.social i{width:22px;height:22px;background:#e4e4e4;display:block}
</style>
</head>
<body>

<header class="site-header">
  <div class="abs menu-block">
    <span style="top:20px"></span><span style="top:35px"></span><span style="top:50px"></span>
  </div>
  <div class="abs brand">Brivora</div>
  <nav class="abs top-nav"><a href="#">Features</a><a href="#" class="active">Login</a></nav>
</header>

<section class="hero">
  <div class="hero-photo" role="img" aria-label="Smiling learner with folded arms in front of a chalkboard with hand-drawn learning doodles"></div>
  <p class="abs hero-intro">Facilitating elegant e-learning and mixed<br>learning solutions for individuals, colleges,<br>organisations and B2B <span class="watch"><i><svg width="10" height="10" viewBox="0 0 10 10"><path d="M2 1l7 4-7 4z" fill="#fff"/></svg></i>WATCH MOVIE</span></p>
  <h1 class="abs hero-title">YOUR LEARNING JOURNEY<br>STARTS HERE</h1>
  <div class="abs join">Join Now!</div>
  <div class="abs search">
    <span>What Can We Help You Learn Today?</span>
    <svg width="24" height="24" viewBox="0 0 24 24"><circle cx="10" cy="10" r="7" fill="none" stroke="#f7b21b" stroke-width="3"/><path d="M15 15l7 7" stroke="#f7b21b" stroke-width="3.5" stroke-linecap="round"/></svg>
  </div>
</section>

<section class="highlights">
  <div class="highlight" style="left:150px">
    <svg width="90" height="66" viewBox="0 0 90 66"><rect x="2" y="2" width="86" height="62" rx="3" fill="#f4f0e8" stroke="#b9b2a6" stroke-width="3"/><rect x="2" y="2" width="86" height="12" fill="#e59a3c"/><rect x="12" y="24" width="26" height="30" fill="#c9c1b3"/><rect x="46" y="24" width="34" height="5" fill="#c9c1b3"/><rect x="46" y="35" width="30" height="5" fill="#c9c1b3"/><rect x="46" y="46" width="34" height="5" fill="#c9c1b3"/></svg>
    <h3>More Than 10 000 Courses</h3>
    <p>Curabitur tincidunt dapibus odio, eu gravida felis blandit vel. Vivamus feugiat auctor lorem non eleifend. Nam eu pellentesque est, vitae interdum nisi.</p>
  </div>
  <div class="highlight" style="left:450px">
    <svg width="80" height="66" viewBox="0 0 80 66"><path d="M40 64C10 42 2 30 2 18A16 16 0 0 1 40 10a16 16 0 0 1 38 8c0 12-8 24-38 46z" fill="#e04a3a"/></svg>
    <h3>Over 5000 Students</h3>
    <p>Nullam dignissim felis diam, sed ultrices est ultrices quis. Maecenas feugiat arcu vitae, et viverra tellus lacinia ut. In hac habitasse platea dictumst.</p>
  </div>
  <div class="highlight" style="left:750px">
    <svg width="90" height="66" viewBox="0 0 90 66"><rect x="10" y="2" width="64" height="44" rx="3" fill="#6f6f6f"/><rect x="15" y="7" width="54" height="34" fill="#dfe9f1"/><rect x="4" y="46" width="76" height="6" rx="2" fill="#8a8a8a"/><rect x="62" y="22" width="26" height="42" rx="3" fill="#4f4f4f"/><rect x="65" y="27" width="20" height="30" fill="#e8c77a"/></svg>
    <h3>Learn At Your Pace On Any Device</h3>
    <p>Aliquam mattis massa ut urna volutpat ultrices. Curabitur tristique enim aliquam, imperdiet felis a, adipiscing odio aliquam phasellus molestie.</p>
  </div>
</section>

<section class="packages">
  <h2 class="section-title" style="top:15px">Discover Learning Packages</h2>
  <div class="abs pack-tabs">
    <span class="tab">Language and Linguistic</span>
    <div class="pack-arrows">
      <i><svg width="8" height="10" viewBox="0 0 8 10"><path d="M7 0L1 5l6 5z" fill="#fff"/></svg></i>
      <i><svg width="8" height="10" viewBox="0 0 8 10"><path d="M1 0l6 5-6 5z" fill="#fff"/></svg></i>
    </div>
  </div>

  <article class="card" style="left:85px">
    <div class="card-cover" role="img" aria-label="Silhouettes of people against a warm orange sunset" style="background:linear-gradient(180deg,#e8a04a,#7a4a25)"><i class="fav"></i></div>
    <p>Cras scelerisque et ante eget lacinia iaculis ullamcorper augue.</p>
    <div class="date">12th August 2015</div>
    <div class="card-meta"><span>● 103</span><span>★ 4.6</span><b>50$</b></div>
  </article>

  <article class="card" style="left:350px">
    <div class="card-cover" style="background:var(--teal)"><i class="fav"></i>
      <svg width="80" height="52" viewBox="0 0 80 52"><rect x="14" y="6" width="60" height="40" fill="#fff"/><path d="M14 6l30 22 30-22" fill="none" stroke="#1fbc9c" stroke-width="3"/><path d="M0 18h10M4 28h8M0 38h10" stroke="#fff" stroke-width="3"/></svg>
    </div>
    <p>Cras scelerisque et ante eget lacinia iaculis ullamcorper augue.</p>
    <div class="date">12th August 2015</div>
    <div class="card-meta"><span>● 103</span><span>★ 4.6</span><b>75$</b></div>
  </article>

  <article class="card" style="left:615px">
    <div class="card-cover" style="background:var(--blue-deep)"><i class="fav"></i>
      <svg width="60" height="66" viewBox="0 0 60 66"><path d="M22 4h16v20l18 34a4 4 0 0 1-4 6H8a4 4 0 0 1-4-6l18-34z" fill="#fff"/><path d="M12 46h36l6 12H6z" fill="#e04a3a"/></svg>
    </div>
    <p>Cras scelerisque et ante eget lacinia iaculis ullamcorper augue.</p>
    <div class="date">12th August 2015</div>
    <div class="card-meta"><span>● 103</span><span>★ 4.6</span><b>75$</b></div>
  </article>

  <article class="card" style="left:880px">
    <div class="card-cover" style="background:var(--sky)"><i class="fav"></i>
      <svg width="60" height="56" viewBox="0 0 60 56"><rect x="4" y="28" width="9" height="24" fill="#fff"/><rect x="18" y="14" width="9" height="38" fill="#fff"/><rect x="32" y="4" width="9" height="48" fill="#fff"/><rect x="46" y="20" width="9" height="32" fill="#fff"/><rect x="0" y="52" width="60" height="3" fill="#fff"/></svg>
    </div>
    <p>Cras scelerisque et ante eget lacinia iaculis ullamcorper augue.</p>
    <div class="date">12th August 2015</div>
    <div class="card-meta"><span>● 103</span><span>★ 4.6</span><b>75$</b></div>
  </article>

  <div class="abs browse">Browse Packages</div>
</section>

<section class="how">
  <div class="abs how-art" role="img" aria-label="Flat illustration of a video player window and course screens with two raised hands"></div>
  <h2>How It Works</h2>
  <p style="top:120px">Sed ut perspiciatis unde omnis iste natus error sit voluptatem accusantium doloremque laudantium, totam rem aperiam, eaque ipsa quae ab illo inventore veritatis et quasi architecto beatae vitae dicta sunt explicabo. Nemo enim ipsam voluptatem quia voluptas sit aspernatur aut odit aut fugit, sed quia consequuntur magni dolores eos qui ratione voluptatem sequi nesciunt.</p>
  <p style="top:240px">Neque porro quisquam est, qui dolorem ipsum quia dolor sit amet, consectetur, adipisci velit, sed quia non numquam eius modi tempora incidunt ut labore et dolore magnam aliquam quaerat voluptatem. Ut enim ad minima veniam, quis nostrum exercitationem ullam corporis suscipit laboriosam, nisi ut aliquid ex ea commodi consequatur. Quis autem vel eum iure reprehenderit qui in ea voluptate velit esse quam nihil molestiae consequatur, vel illum qui dolorem eum fugiat quo voluptas nulla pariatur.</p>
</section>

<section class="progress">
  <h2 class="section-title" style="top:30px">Track Your Progres</h2>
  <p class="lead">Neque porro quisquam est, qui dolorem ipsum quia dolor sit amet, consectetur, adipisci velit, sed<br>quia non numquam eius modi tempora incidunt ut labore et dolore</p>
  <svg class="abs" style="left:0;top:140px" width="1200" height="180" viewBox="0 0 1200 180">
    <polyline points="0,170 85,160 230,140 360,120 530,100 630,118 735,98" fill="none" stroke="#5aa1dc" stroke-width="5"/>
    <polyline points="735,98 935,76 1110,56 1200,48" fill="none" stroke="#5aa1dc" stroke-width="5" opacity=".45"/>
    <g fill="#5aa1dc"><circle cx="85" cy="160" r="9"/><circle cx="360" cy="120" r="9"/><circle cx="530" cy="100" r="9"/><circle cx="630" cy="118" r="9"/></g>
    <g fill="#dfe6ec"><circle cx="935" cy="76" r="10"/><circle cx="1110" cy="56" r="10"/></g>
    <path d="M735 98c-12-14-22-24-22-36a22 22 0 0 1 44 0c0 12-10 22-22 36z" fill="#c9413a"/>
    <circle cx="735" cy="62" r="8" fill="#fff"/>
  </svg>
  <h2 class="section-title" style="top:395px">And Your Skills</h2>
  <svg class="abs" style="left:0;top:480px" width="1200" height="140" viewBox="0 0 1200 140">
    <g transform="translate(385 70)">
      <circle r="60" fill="none" stroke="#e6e6e6" stroke-width="9"/>
      <circle r="60" fill="none" stroke="#5aa1dc" stroke-width="9" stroke-dasharray="320.4 377" transform="rotate(-90)"/>
      <text y="10" text-anchor="middle" font-size="28" fill="#5aa1dc" font-family="Open Sans, sans-serif">85%</text>
    </g>
    <g transform="translate(600 70)">
      <circle r="60" fill="none" stroke="#e6e6e6" stroke-width="9"/>
      <circle r="60" fill="none" stroke="#f7b21b" stroke-width="9" stroke-dasharray="245 377" transform="rotate(-90)"/>
      <text y="10" text-anchor="middle" font-size="28" fill="#f7b21b" font-family="Open Sans, sans-serif">65%</text>
    </g>
    <g transform="translate(815 70)">
      <circle r="60" fill="none" stroke="#e6e6e6" stroke-width="9"/>
      <circle r="60" fill="none" stroke="#1fbc9c" stroke-width="9" stroke-dasharray="301.6 377" transform="rotate(-90)"/>
      <text y="10" text-anchor="middle" font-size="28" fill="#1fbc9c" font-family="Open Sans, sans-serif">80%</text>
    </g>
  </svg>
  <span class="skill-label" style="left:285px;top:630px">Web design</span>
  <span class="skill-label" style="left:500px;top:630px">Branding design</span>
  <span class="skill-label" style="left:715px;top:630px">Time management</span>
</section>

<section class="devices">
  <div class="devices-photo" role="img" aria-label="Person sitting outdoors using a smartphone"></div>
  <h2>On Any Device</h2>
  <p>Lorem ipsum dolor sit amet, consectetur adipiscing elit, sed do eiusmod tempor incididunt ut labore et dolore magna aliqua.</p>
  <div class="badge" style="left:85px;width:160px;background:#1c1c1c;border:1px solid #777"></div>
  <div class="badge" style="left:268px;width:160px;background:#f2f2f2"></div>
  <div class="badge" style="left:451px;width:160px;background:#8b3fa3"></div>
</section>

<section class="voices">
  <h2 class="section-title" style="top:55px">What People Say</h2>
  <div class="voice" style="left:200px;top:150px">
    <svg width="120" height="130" viewBox="0 0 120 130"><path d="M60 2l54 31v64l-54 31-54-31V33z" fill="#e9dcd0" stroke="#2f3b48" stroke-width="8" role="img" aria-label="Portrait of a smiling student"/><path d="M10 95l50 29 50-29" fill="none" stroke="#1fbc9c" stroke-width="8"/></svg>
    <div class="name">Excepteur sint occaecat</div>
    <div class="quote">Sed non mauris vitae erat consequat auctor eu in elit. Class aptent taciti sociosqu ad litora torquent per.</div>
  </div>
  <div class="voice" style="left:640px;top:150px">
    <svg width="120" height="130" viewBox="0 0 120 130"><path d="M60 2l54 31v64l-54 31-54-31V33z" fill="#d7c6b6" stroke="#2f3b48" stroke-width="8" role="img" aria-label="Portrait of a student wearing glasses"/><path d="M10 95l50 29 50-29" fill="none" stroke="#1fbc9c" stroke-width="8"/></svg>
    <div class="name">Excepteur sint occaecat</div>
    <div class="quote">Sed non mauris vitae erat consequat auctor eu in elit. Class aptent taciti sociosqu ad litora torquent per.</div>
  </div>
  <div class="voice" style="left:200px;top:295px">
    <svg width="120" height="130" viewBox="0 0 120 130"><path d="M60 2l54 31v64l-54 31-54-31V33z" fill="#e2d3c5" stroke="#2f3b48" stroke-width="8" role="img" aria-label="Portrait of a smiling learner"/><path d="M10 95l50 29 50-29" fill="none" stroke="#1fbc9c" stroke-width="8"/></svg>
    <div class="name">Excepteur sint occaecat</div>
    <div class="quote">Sed non mauris vitae erat consequat auctor eu in elit. Class aptent taciti sociosqu ad litora torquent per.</div>
  </div>
  <div class="voice" style="left:640px;top:295px">
    <svg width="120" height="130" viewBox="0 0 120 130"><path d="M60 2l54 31v64l-54 31-54-31V33z" fill="#d9c9b9" stroke="#2f3b48" stroke-width="8" role="img" aria-label="Portrait of a bearded learner"/><path d="M10 95l50 29 50-29" fill="none" stroke="#1fbc9c" stroke-width="8"/></svg>
    <div class="name">Excepteur sint occaecat</div>
    <div class="quote">Sed non mauris vitae erat consequat auctor eu in elit. Class aptent taciti sociosqu ad litora torquent per.</div>
  </div>
</section>

<footer class="site-footer">
  <ul class="abs foot-links">
    <li>Home</li><li>About us</li><li>Features</li><li>Blog</li><li>Pricing</li><li>Careers</li><li>Support</li><li>Contact us</li>
  </ul>
  <div class="abs foot-col" style="left:280px;top:40px;width:260px">
    <h4>Brivora</h4>
    <p style="margin-bottom:14px">Learning for Organisations and Educational Institutions Launching Soon!</p>
    <p>Brivora will be launching shortly to improve learning for organisations and educators, with interactive and blended learning tools for every team. <span style="color:var(--orange)">hello@brivora-learn.test</span></p>
  </div>
  <div class="abs foot-col" style="left:610px;top:40px;width:260px">
    <h4>LAST TWEETS</h4>
    <div class="tweet"><i></i><p>New blended courses for teams are now open for early sign up.<br><span style="color:#999">3 months ago</span></p></div>
    <div class="tweet"><i></i><p>Study tips: short daily sessions beat long weekly ones.<br><span style="color:#999">3 months ago</span></p></div>
    <div class="tweet"><i></i><p>Thank you to all our learners for a great first term.<br><span style="color:#999">3 months ago</span></p></div>
  </div>
  <div class="abs foot-col" style="left:920px;top:40px;width:200px">
    <h4>NEWSLETTER</h4>
    <p style="margin-bottom:14px">Receive course updates, study advice and news straight to your inbox.</p>
    <div style="display:flex;gap:4px;margin-bottom:26px"><div class="field"></div><div class="go"></div></div>
    <h4 style="font-size:13px;margin-bottom:10px">Follow us</h4>
    <div class="social"><i></i><i></i><i></i><i></i><i></i><i></i></div>
  </div>
  <div class="bar"></div>
</footer>

</body>
</html>
```